TableHop website needs a desktop homepage design

We need a desktop homepage design for TableHop.co.uk, a website to help you to find the best restaurants in each main city of Europe, with initial focus on London. It is not a directory with thousands of restaurants and reviews, else lists of top 20 restaurants for each area of the city. TableHop from all around the city will be able to keep an itinerary of where they eat, showing them later funny stats like "this month you really went for pizzas, don't you?". Keep it funny but professional.

A bit of branding has been done but this project give you total freedom to design the homepage of the site. The design must be a mix between minimal, flat and clean layout. The main idea is to keep it simple, easy to use and showing just the necessary elements.

For the font and colour scheme, we would like to use a thin but energetic font using the #E1393A colour as starting point even if you have freedom to slightly modify it. Blacks, greys and whites can be the secondary colours but we are open to introduce another main colour to the site like green, orange or yellow.

A simple wireframe has been attached to help you but the main elements that the page requires are the next:
- Panoramic fancy image in the header to contain the logo and the search form (the fields of the form are specified on the wireframe) and maybe some animated text to fill the right gap.
- List of results (10 results per page) showing the main info for each restaurant: name, thumbnail, location (zone, area), category, price, description, rating (no with stars please) and whatever you want to add that makes sense.
- Right hand sidebar with 3 widgets: Categories, Location and prices.

You can get the icons from glyphbarn.net.

We are open to have some text-shadows, rounded corners, box-shadows but trying to keep it minimal, flat and clean as much as possible. The main attractive of the site are the food/restaurant images.

Target Market(s)

22 - 45 TableHop lovers from the city. busy people that want to disconnect and relax through the food. The don't mind to pay for quality and new experiences. Up to meet new places around them.

Industry/Entity Type

Restaurant

Requirements
Must have
• Panoramic image in the header, restaurants search form as per wireframe, list results with pagination, right hand sidebar with the widgets mention above and a nice footer with extra elements like "latest restaurants, latest tweets, etc.."
Nice to have
• This site will only be supported by the latest browsers so the idea is to have nice CSS3 transitions all around. Have that in mind at the time to design it even if you cannot show it on the design.
Should not have
• Busy backgrounds and unnecessary images that would slow down the page load.

```html
<!DOCTYPE html>
<html lang="en">
<head>
<meta charset="utf-8">
<title>TableHop in London</title>
<link rel="stylesheet" href="https://fonts.googleapis.com/css2?family=Ubuntu:wght@400;500;700&family=Source+Sans+3:wght@400;600&display=swap">
<style>
:root{
  --red:#f0432a;
  --red-dark:#c9301d;
  --ink:#555;
  --text:#444;
  --grey-bar:#dcdcdc;
  --line:#cfcfcf;
  --green:#7cc02a;
  --yellow:#f5b800;
  --blue:#1c9ad6;
  --stripe-red:#d42a20;
}
*{box-sizing:border-box;margin:0;padding:0}
html,body{width:1200px;height:1166px;overflow:hidden;background:#fff}
body{position:relative;font-family:"Source Sans 3",sans-serif;color:var(--text)}
.topbar{position:absolute;left:0;top:0;width:1200px;height:100px;background:linear-gradient(#2e2e2e,#1f1f1f)}
.brand{position:absolute;left:106px;top:28px;display:flex;align-items:baseline;gap:12px}
.brand-name{font-family:"Ubuntu",sans-serif;font-weight:500;font-size:36px;color:var(--red)}
.brand-tag{font-family:"Ubuntu",sans-serif;font-size:16px;color:#fff}
.account{position:absolute;right:122px;top:46px;display:flex;gap:34px;font-family:"Ubuntu",sans-serif;font-weight:500;font-size:18px;color:#fff}
.stripe{position:absolute;left:0;top:100px;width:1200px;height:4px;
  background:linear-gradient(90deg,var(--stripe-red) 0 25%,var(--green) 25% 50%,var(--yellow) 50% 75%,var(--blue) 75% 100%);
  background-size:500px 4px;background-position:-79px 0}
.hero{position:absolute;left:0;top:104px;width:1200px;height:651px;
  background:
    radial-gradient(ellipse 260px 120px at 640px 620px,rgba(245,245,240,.85),transparent 70%),
    radial-gradient(ellipse 220px 90px at 900px 600px,rgba(240,240,235,.7),transparent 70%),
    radial-gradient(circle 110px at 720px 490px,#f2c44a,transparent 70%),
    radial-gradient(circle 90px at 850px 300px,#4e8a22,transparent 70%),
    radial-gradient(circle 80px at 660px 150px,#4a7f20,transparent 70%),
    radial-gradient(circle 110px at 960px 160px,#86b82a,transparent 70%),
    radial-gradient(circle 120px at 1130px 330px,#e2542a,transparent 70%),
    radial-gradient(circle 130px at 620px 360px,#e8502a,transparent 70%),
    radial-gradient(circle 90px at 780px 420px,#d8442a,transparent 70%),
    radial-gradient(circle 100px at 1000px 430px,#7a5a30,transparent 70%),
    radial-gradient(ellipse 700px 460px at 700px 340px,#b56a2a,#6b4020 55%,#241a14 85%,#14100c)}
.search{position:absolute;left:101px;top:270px;width:494px;height:382px;background:#fff;border-radius:150px 170px 160px 170px/140px 160px 170px 150px;box-shadow:0 6px 18px rgba(0,0,0,.35)}
.search h1{position:absolute;left:0;width:100%;top:48px;text-align:center;font-family:"Ubuntu",sans-serif;font-weight:500;font-size:26px;line-height:31px;color:var(--ink)}
.field{position:absolute;width:172px}
.field label{display:block;font-family:"Ubuntu",sans-serif;font-size:17px;color:var(--ink);margin-bottom:10px}
.select{height:31px;border:1px solid #ccc;border-radius:3px;background:linear-gradient(#fff,#f0f0f0);position:relative;margin-left:2px}
.select::after{content:"";position:absolute;right:6px;top:8px;width:13px;height:13px;border:1px solid #555;background:linear-gradient(#fff,#ddd)}
.select::before{content:"";position:absolute;right:10px;top:13px;border:3px solid transparent;border-top:4px solid #222;z-index:1}
.btn-find{position:absolute;left:141px;top:291px;width:224px;height:42px;border-radius:21px;background:linear-gradient(var(--red),var(--red-dark));box-shadow:0 2px 3px rgba(0,0,0,.3);color:#fff;font-family:"Ubuntu",sans-serif;font-weight:700;font-size:22px;text-align:center;line-height:42px}
.cutlery{position:absolute;background:linear-gradient(90deg,#8a8a8a,#e4e4e4,#8a8a8a);border-radius:8px}
.host{position:absolute;left:968px;top:660px;width:134px;height:96px;border-radius:40px 40px 0 0;background:linear-gradient(rgba(60,40,30,.55),rgba(200,60,40,.75))}
.section-title{position:absolute;left:115px;top:782px;display:flex;align-items:center;gap:12px;font-family:"Ubuntu",sans-serif;font-weight:500;font-size:29px;color:var(--ink)}
.rule{position:absolute;left:121px;top:828px;width:684px;border-top:1px solid var(--line)}
.thumb{position:absolute;left:121px;top:854px;width:231px;height:158px;border:3px solid #bbb;background:linear-gradient(135deg,#6b5a48,#3a2f26 50%,#9a8a70)}
.result-name{position:absolute;left:371px;top:851px;font-family:"Ubuntu",sans-serif;font-weight:500;font-size:18px;color:var(--ink)}
.result-text{position:absolute;left:121px;top:890px;width:680px;font-size:13.5px;line-height:18px;color:var(--text)}
.result-text::before{content:"";float:left;width:250px;height:126px}
.meta{position:absolute;left:122px;top:1077px;width:683px;height:52px;background:var(--grey-bar);padding:0 8px 0 19px;display:flex;align-items:center;justify-content:space-between;font-size:13.5px}
.btn-book{background:var(--red);color:#fff;border-radius:3px;width:96px;height:34px;line-height:34px;text-align:center}
.widget{position:absolute;left:864px;width:254px}
.widget-head{height:46px;background:var(--red);border-radius:3px;display:flex;align-items:center;justify-content:space-between;padding:0 18px 0 20px;color:#fff;font-family:"Ubuntu",sans-serif;font-weight:700;font-size:26px}
.widget ul{list-style:none;padding-left:30px;font-size:13.5px;line-height:30px;color:var(--text)}
</style>
</head>
<body>
<header class="topbar">
  <div class="brand"><span class="brand-name">TableHop</span><span class="brand-tag">in london</span></div>
  <nav class="account"><span>Login</span><span>Register</span></nav>
</header>
<div class="stripe"></div>

<section class="hero" role="img" aria-label="Close-up photograph of a plate of rice with roasted vegetables, carrots, cauliflower and broccoli"></section>

<form class="search">
  <div class="cutlery" role="img" aria-label="Fork illustration" style="left:26px;top:112px;width:12px;height:256px"></div>
  <div class="cutlery" role="img" aria-label="Knife illustration" style="left:446px;top:96px;width:16px;height:262px"></div>
  <h1>Enter Your Location to find<br>Restaurant Near You</h1>
  <div class="field" style="left:65px;top:129px"><label>What Restaurant?</label><div class="select"></div></div>
  <div class="field" style="left:257px;top:128px"><label>What Kind of Food?</label><div class="select"></div></div>
  <div class="field" style="left:65px;top:203px"><label>Where?</label><div class="select"></div></div>
  <div class="field" style="left:257px;top:203px"><label>Prices?</label><div class="select"></div></div>
  <div class="btn-find">Find Restaurant</div>
</form>

<div class="host" role="img" aria-label="Cartoon hostess character peeking over the sidebar"></div>

<h2 class="section-title">
  <svg width="32" height="32" viewBox="0 0 32 32"><circle cx="16" cy="16" r="14" fill="none" stroke="#555" stroke-width="3"/><circle cx="16" cy="16" r="8" fill="#555"/></svg>
  Best Restaurants in London
</h2>
<div class="rule"></div>

<article class="result">
  <div class="thumb" role="img" aria-label="Photo of the restaurant dining room with a meal on the table"></div>
  <h3 class="result-name">Ember &amp; Oak Seven Dials</h3>
  <p class="result-text">The original Ember &amp; Oak in Spitalfields is a great bar and grill – but this newer branch is a truly sensational one. The entrance is a bit hidden, despite the Covent Garden location, but once inside it’s a real beauty of a basement which looks as if it’s been there a century – in fact, it only opened as a restaurant at the end of 2010. The meat’s better quality, and better cooked, than at many more expensive Mayfair steak restaurants. Ember &amp; Oak’s not cheap, though – you’ll easily part with more than £50 per head, but dining here’s quite an experience, and very ‘now’. When to go: When your carnal urges will only be satisfied by something big and bloody.</p>
  <div class="meta"><span>24 Marlow Lane, WC2H 4QT</span><span class="btn-book">Book Now</span></div>
</article>

<aside class="sidebar">
  <div class="widget" style="top:755px">
    <div class="widget-head">Categories
      <svg width="34" height="28" viewBox="0 0 34 28" fill="#fff"><circle cx="17" cy="4" r="2.5"/><path d="M3 21a14 14 0 0 1 28 0z"/><rect x="0" y="23" width="34" height="4" rx="1"/></svg>
    </div>
    <ul style="padding-top:9px"><li>Italian Restaurant (2)</li><li>Indian Restaurant (1)</li></ul>
  </div>
  <div class="widget" style="top:887px">
    <div class="widget-head">Location
      <svg width="18" height="30" viewBox="0 0 18 30" fill="#fff"><circle cx="9" cy="8" r="7"/><rect x="8" y="14" width="2" height="14"/><ellipse cx="9" cy="28" rx="6" ry="1.5"/></svg>
    </div>
    <ul style="padding-top:18px"><li>Restaurants in West London (2)</li><li>Restaurants in West London (1)</li></ul>
  </div>
  <div class="widget" style="top:1037px">
    <div class="widget-head">Prices
      <svg width="40" height="26" viewBox="0 0 40 26" fill="none" stroke="#fff" stroke-width="2"><rect x="6" y="1" width="32" height="16"/><rect x="4" y="4" width="32" height="16" fill="#f0432a"/><rect x="2" y="8" width="32" height="16" fill="#f0432a"/><circle cx="18" cy="16" r="4"/></svg>
    </div>
    <ul style="padding-top:16px"><li>Casual Restaurants ( €10 - €20)  (22)</li><li>Casual Restaurants ( €10 - €20)  (22)</li></ul>
  </div>
</aside>
</body>
</html>
```